Building Company Business Card Design

Need a design for a business card:
It needs to have: Name, Phone, Facebook link, Website, email
i would also like a list of works we undertake:
-New Homes
-Extensions, Renovations & Bathrooms
-Decking, Carports, Sheds (Residential and Industrial)
-Carpentry
-Fences, Patios & Pergolas

Contact Information for Business Card

Name, Phone, Facebook link, Website, email + details of services provided listed in description

```html
<!DOCTYPE html>
<html lang="en">
<head>
<meta charset="utf-8">
<title>Ridgeline Homes – Business Card</title>
<link rel="stylesheet" href="https://fonts.googleapis.com/css2?family=Arimo:wght@400;700&display=swap">
<style>
  :root {
    --backdrop: #a3a3a3;
    --card-light: #fbfbfb;
    --card-dark: #2c2c2c;
    --brand-green: #2fae4a;
    --ink: #2a2a2a;
    --ink-soft: #6e6e6e;
    --rule: #c9c9c9;
    --on-dark: #f2f2f2;
  }
  * { box-sizing: border-box; margin: 0; padding: 0; }
  html, body {
    width: 1200px; height: 1050px; overflow: hidden;
    background: var(--backdrop);
    font-family: "Arimo", Arial, sans-serif;
  }
  .sheet {
    position: relative; width: 1200px; height: 1050px;
    display: flex; flex-direction: column; align-items: center; justify-content: center; gap: 70px;
  }
  .card {
    position: relative; width: 700px; height: 400px; border-radius: 26px;
    box-shadow: 0 10px 28px rgba(0,0,0,.22);
  }
  .card--front { background: var(--card-light); color: var(--ink); }
  .card--back { background: var(--card-dark); color: var(--on-dark); border: 3px solid #e9e9e9; }

  .wordmark {
    position: absolute; left: 0; right: 0;
    display: flex; align-items: center; justify-content: center; gap: 16px;
  }
  .wordmark__square { width: 34px; height: 34px; background: var(--brand-green); flex: none; }
  .wordmark__text { font-weight: 700; text-transform: uppercase; line-height: 1.05; letter-spacing: .04em; }
  .wordmark__text span { display: block; }
  .card--front .wordmark { top: 66px; }
  .card--front .wordmark__text { color: var(--ink); font-size: 40px; }
  .card--front .wordmark__text span + span { font-size: 21px; letter-spacing: .09em; }
  .card--back .wordmark { top: 70px; }
  .card--back .wordmark__text { color: var(--on-dark); font-size: 50px; }
  .card--back .wordmark__text span + span { font-size: 26px; letter-spacing: .09em; }

  .identity {
    position: absolute; left: 110px; top: 228px; width: 210px; text-align: right;
  }
  .identity__name { color: var(--brand-green); font-weight: 700; font-size: 30px; }
  .identity__role { color: var(--ink-soft); font-size: 21px; margin-top: 4px; }
  .divider { position: absolute; left: 342px; top: 222px; width: 2px; height: 112px; background: var(--rule); }

  .contacts { position: absolute; left: 366px; top: 226px; list-style: none; }
  .contacts li { display: flex; align-items: center; gap: 10px; font-size: 20px; line-height: 27px; }
  .contacts svg { width: 17px; height: 17px; flex: none; fill: var(--brand-green); }

  .services {
    position: absolute; left: 0; right: 0; top: 236px; text-align: center;
    font-size: 21px; line-height: 29px; list-style: none;
  }
  .services .bullet {
    display: inline-block; width: 7px; height: 7px; background: var(--brand-green);
    margin: 0 14px 4px; vertical-align: middle;
  }
</style>
</head>
<body>
<main class="sheet">

  <section class="card card--front" aria-label="Business card front">
    <div class="wordmark">
      <div class="wordmark__square"></div>
      <div class="wordmark__text"><span>Ridgeline Homes</span><span>and Builds Pty Ltd</span></div>
    </div>
    <div class="identity">
      <p class="identity__name">Marcus Hale</p>
      <p class="identity__role">President</p>
    </div>
    <div class="divider"></div>
    <ul class="contacts">
      <li>
        <svg viewBox="0 0 24 24"><path d="M6.6 10.8a15.1 15.1 0 0 0 6.6 6.6l2.2-2.2a1 1 0 0 1 1-.25 11.4 11.4 0 0 0 3.6.57 1 1 0 0 1 1 1V20a1 1 0 0 1-1 1A17 17 0 0 1 3 4a1 1 0 0 1 1-1h3.5a1 1 0 0 1 1 1c0 1.25.2 2.45.57 3.57a1 1 0 0 1-.25 1z"/></svg>
        (555) 0142-7788
      </li>
      <li>
        <svg viewBox="0 0 24 24"><path d="M2 5h20v14H2z M4 7v.5l8 5 8-5V7l-8 5z" fill-rule="evenodd"/></svg>
        info@ridgelinehomes.com
      </li>
      <li>
        <svg viewBox="0 0 24 24"><circle cx="12" cy="12" r="10"/><path d="M2 12h20M12 2c3 3 3 17 0 20M12 2c-3 3-3 17 0 20" stroke="#fff" stroke-width="1.4" fill="none"/></svg>
        www.ridgelinehomes.com
      </li>
      <li>
        <svg viewBox="0 0 24 24"><circle cx="12" cy="12" r="10"/></svg>
        @ridgelinehomes
      </li>
    </ul>
  </section>

  <section class="card card--back" aria-label="Business card back">
    <div class="wordmark">
      <div class="wordmark__square"></div>
      <div class="wordmark__text"><span>Ridgeline Homes</span><span>and Builds Pty Ltd</span></div>
    </div>
    <ul class="services">
      <li>New Homes<span class="bullet"></span>Extensions, Renovations &amp; Bathrooms</li>
      <li>Decking, Carports, Sheds (Residential and Industrial)</li>
      <li>Carpentry<span class="bullet"></span>Fences, Patios &amp; Pergolas</li>
    </ul>
  </section>

</main>
</body>
</html>
```